Happy Birthday Cards (from Law Firm)

Need classy, professional AND polished Happy Birthday Cards from law firm.

Please tie in the firm logo and colors somewhere with the picture on front or inside(but not used too many times)

Include company logo somewhere on the card, firm name (Verona Pask Law, PLLC) www.veronapasklaw.com
Updates

Reason: Thank you for your patience. Had a family emergency.

Target Market(s)

Law firm clients ages 30 - 99

Industry/Entity Type

Law Firm

Font styles to use
Serif
Sans Serif
Decorative
Script

Requirements
Must have
• Must be classy, elegant, professional, polished from a business
• Birthday wish or message - you suggest one.
• For example "Enjoy every moment of your life. May everyday bring something new and exciting for you. May your birthday be as amazing as you."
Nice to have
• Would like several birthday card templates (for male/for female); traditional/fun

```html
<!DOCTYPE html>
<html lang="en">
<head>
<meta charset="utf-8">
<title>Birthday Card – Verona Pask Law, PLLC</title>
<link rel="stylesheet" href="https://fonts.googleapis.com/css2?family=Playfair+Display:wght@400;700&display=swap">
<style>
  :root {
    --bg: #2b2b2d;
    --teal-light: #0f8f9a;
    --teal-dark: #0f4f78;
    --teal-emboss: #1a9aa8;
    --teal-deep: #0c5f7c;
    --navy: #163f6b;
    --ink: #1d4c7a;
    --paper: #ffffff;
    --paper-shade: #f1f3f5;
    --rule: #5d6d7d;
    --gift-light: #8ec8e8;
    --gift-dark: #2a6fb3;
  }
  * { margin: 0; padding: 0; box-sizing: border-box; }
  html, body {
    width: 1200px; height: 900px; overflow: hidden;
    background: var(--bg);
  }
  .canvas { position: relative; width: 1200px; height: 900px; }
  .card {
    position: absolute; left: 250px; width: 700px; height: 400px;
    box-shadow: 0 10px 30px rgba(0,0,0,.45);
    overflow: hidden;
  }
  .card--front {
    top: 30px;
    background: linear-gradient(135deg, var(--teal-light) 0%, var(--teal-dark) 70%);
  }
  .front__greeting {
    position: absolute; left: 180px; top: 80px; width: 340px; height: 240px;
    display: flex; flex-direction: column; justify-content: center; align-items: center;
    font-family: "Playfair Display", serif;
    font-size: 66px; font-weight: 700; line-height: 1.05;
    color: var(--teal-deep);
    text-shadow: 1px 1px 0 var(--teal-emboss);
  }
  .card--inside {
    top: 470px;
    background: linear-gradient(90deg, var(--paper-shade), var(--paper) 40%);
  }
  .band { position: absolute; height: 14px; background: var(--navy); }
  .band--top { left: 480px; right: 0; top: 140px; }
  .band--bottom { left: 0; width: 300px; top: 262px; }
  .message {
    position: absolute; left: 40px; top: 110px; width: 425px;
    text-align: center; color: var(--ink);
    font-family: "Playfair Display", serif;
  }
  .message__title {
    font-size: 15px; letter-spacing: 5px; font-weight: 400; white-space: nowrap;
  }
  .message__line {
    font-size: 16px; font-weight: 700; line-height: 1.4; white-space: nowrap;
  }
  .photo {
    position: absolute; left: 0; top: 278px; width: 310px; height: 122px;
    background: linear-gradient(90deg, var(--gift-light) 0%, var(--gift-dark) 45%, #e9eef5 60%, var(--gift-light) 100%);
  }
  .firm {
    position: absolute; left: 520px; top: 180px; width: 165px;
    text-align: center; color: var(--ink);
    font-family: "Playfair Display", serif;
  }
  .firm__mark {
    width: 44px; height: 44px; border-radius: 50%;
    background: var(--navy); margin: 0 auto 8px;
  }
  .firm__name {
    font-size: 20px; font-weight: 400; white-space: nowrap;
    padding-bottom: 4px; border-bottom: 1px solid var(--rule);
  }
  .firm__type {
    font-size: 9px; letter-spacing: 2px; margin-top: 4px;
    padding-bottom: 6px; border-bottom: 1px solid var(--rule);
  }
</style>
</head>
<body>
<main class="canvas">
  <section class="card card--front">
    <h1 class="front__greeting"><span>Happy</span><span>Birthday</span></h1>
  </section>

  <section class="card card--inside">
    <div class="band band--top"></div>
    <div class="message">
      <p class="message__title">ENJOY EVERY MOMENT OF YOUR LIFE</p>
      <p class="message__line">May everyday bring something new and exciting for you.</p>
      <p class="message__line">May your birthday be as amazing as you.</p>
    </div>
    <div class="band band--bottom"></div>
    <div class="photo" role="img" aria-label="Photo of a blue gift box with polka-dot ribbon and a cupcake with a candle"></div>
    <div class="firm">
      <div class="firm__mark"></div>
      <p class="firm__name">Verona Pask</p>
      <p class="firm__type">LAW PLLC</p>
    </div>
  </section>
</main>
</body>
</html>
```